BRAMWELL Sofa Shop - Hipster Hero Header Design

I want to use the 'Meridale' theme on Storvik

https://meridale-theme-basic.storvikshop.example/
https://themes.storvikshop.example/themes/meridale/styles/plenwise/preview

The main, PRIMARY thing that I need designed is the top hero header to be customized to my shop. Please use the attached examples as a reference. I welcome creativity. I do like the hipster vibe. I'd like a sofa/Living Room theme.

****To be clear...I want a hipster header designed...I love the creative fonts on a filtered relevant photo*** I have placed attachments. Hipster fonts or a Badge, or some combo. If you need guidance please look at examples.

Words on design should be:

BRAMWELL SOFA SHOP.

(I will separately handle the functionality of the site.)
Thanks.
Updates

Please check my brief as I have streamlined my desires. I simply want a hero header designed and 3 buttons designed. Examples of hero headers are attached. Thanks. Added Saturday, September 26, 2015

Target Market(s)

Sofa Shoppers

Industry/Entity Type

Furniture Store

Number of Pages Required

1 page

Requirements
Nice to have
• Bramwell Sofa Shop
• https://meridale-theme-basic.storvikshop.example/

```html
<!DOCTYPE html>
<html lang="en">
<head>
<meta charset="utf-8">
<title>Bramwell Sofa Shop – Hero Header Options</title>
<link rel="stylesheet" href="https://fonts.googleapis.com/css2?family=Alfa+Slab+One&family=Cormorant+Garamond:wght@300&family=Oswald:wght@300;400&family=Anton&family=Open+Sans:wght@400;600&display=swap">
<style>
  :root {
    --sheet-black: #0b0b0b;
    --label-text: #f2f2f2;
    --photo-light: #8a8a8a;
    --photo-mid: #5c5c5c;
    --photo-dark: #2e2e2e;
    --sofa-shade: #141414;
    --ink-white: #ffffff;
    --nav-text: #e6e6e6;
  }
  * { margin: 0; padding: 0; box-sizing: border-box; }
  html, body { width: 1200px; height: 2600px; overflow: hidden; background: var(--sheet-black); }
  body { font-family: "Open Sans", Arial, sans-serif; }

  .option { position: relative; width: 1200px; height: 650px; }
  .option-label {
    height: 40px; background: var(--sheet-black); color: var(--label-text);
    font-size: 20px; line-height: 40px; padding-left: 14px;
  }
  .hero { position: relative; height: 610px; overflow: hidden; }
  .hero-photo {
    position: absolute; inset: 0;
    background:
      radial-gradient(ellipse 46% 20% at 50% 50%, var(--sofa-shade) 0%, rgba(20,20,20,0.85) 55%, rgba(20,20,20,0) 100%),
      linear-gradient(180deg, transparent 62%, rgba(0,0,0,0.25) 63%, transparent 80%),
      radial-gradient(ellipse 75% 70% at 50% 45%, var(--photo-light) 0%, var(--photo-mid) 55%, var(--photo-dark) 100%);
  }

  .nav { position: absolute; display: flex; gap: 24px; font-size: 14px; letter-spacing: 0.5px;
         text-transform: uppercase; color: var(--nav-text); }

  .brand { position: absolute; left: 0; right: 0; text-align: center; color: var(--ink-white); }
  .brand-name, .brand-sub { display: block; white-space: nowrap; }

  /* Option 1 – slab serif, nav top right */
  .hero--slab .nav { top: 70px; right: 40px; }
  .hero--slab .brand { top: 230px; font-family: "Alfa Slab One", Georgia, serif; }
  .hero--slab .brand-name { font-size: 84px; line-height: 1; letter-spacing: 3px;
                            color: transparent; -webkit-text-stroke: 2px var(--ink-white); }
  .hero--slab .brand-sub { font-size: 56px; line-height: 1.2; letter-spacing: 2px; }

  /* Option 2 – fine serif, centred nav bar */
  .hero--serif .nav-bar { position: absolute; top: 0; left: 0; right: 0; height: 36px; background: var(--sheet-black); }
  .hero--serif .nav { top: 9px; left: 0; right: 0; justify-content: center; font-size: 13px; }
  .hero--serif .brand { top: 205px; font-family: "Cormorant Garamond", Georgia, serif; font-weight: 300; }
  .hero--serif .brand-name { font-size: 112px; line-height: 1; letter-spacing: 6px; }
  .hero--serif .brand-sub { font-size: 62px; line-height: 1.25; letter-spacing: 4px; }

  /* Option 3 – condensed sans between rules, nav top left */
  .hero--condensed .nav { top: 12px; left: 20px; font-size: 13px; }
  .hero--condensed .brand { top: 170px; font-family: "Oswald", "Arial Narrow", sans-serif; font-weight: 300; }
  .hero--condensed .rule { display: block; width: 560px; height: 2px; margin: 0 auto; background: var(--ink-white); }
  .hero--condensed .brand-name { font-size: 130px; line-height: 1.12; letter-spacing: 4px; font-weight: 400; }
  .hero--condensed .brand-sub { font-size: 86px; line-height: 1.12; letter-spacing: 2px; }

  /* Option 4 – heavy display, nav bottom centre */
  .hero--heavy .brand { top: 140px; font-family: "Anton", Impact, sans-serif; }
  .hero--heavy .brand-name { font-size: 150px; line-height: 1.05; letter-spacing: 4px; }
  .hero--heavy .brand-sub { font-size: 108px; line-height: 1.05; letter-spacing: 6px; }
  .hero--heavy .nav { bottom: 40px; left: 0; right: 0; justify-content: center; font-size: 13px; }
</style>
</head>
<body>

<section class="option">
  <div class="option-label">Option #1</div>
  <div class="hero hero--slab">
    <div class="hero-photo" role="img" aria-label="Filtered grey photo of a dark curved sofa in a studio"></div>
    <nav class="nav"><span>About</span><span>Products</span><span>Contact</span></nav>
    <h1 class="brand"><span class="brand-name">BRAMWELL</span><span class="brand-sub">SOFA SHOP</span></h1>
  </div>
</section>

<section class="option">
  <div class="option-label">Option #2</div>
  <div class="hero hero--serif">
    <div class="hero-photo" role="img" aria-label="Filtered grey photo of a dark curved sofa in a studio"></div>
    <div class="nav-bar"></div>
    <nav class="nav"><span>About</span><span>Products</span><span>Contact</span></nav>
    <h1 class="brand"><span class="brand-name">BRAMWELL</span><span class="brand-sub">SOFA SHOP</span></h1>
  </div>
</section>

<section class="option">
  <div class="option-label">Option #3</div>
  <div class="hero hero--condensed">
    <div class="hero-photo" role="img" aria-label="Filtered grey photo of a dark curved sofa in a studio"></div>
    <nav class="nav"><span>About</span><span>Products</span><span>Contact</span></nav>
    <h1 class="brand">
      <span class="rule"></span>
      <span class="brand-name">BRAMWELL</span>
      <span class="brand-sub">SOFA SHOP</span>
      <span class="rule"></span>
    </h1>
  </div>
</section>

<section class="option">
  <div class="option-label">Option #4</div>
  <div class="hero hero--heavy">
    <div class="hero-photo" role="img" aria-label="Filtered grey photo of a dark curved sofa in a studio"></div>
    <h1 class="brand"><span class="brand-name">BRAMWELL</span><span class="brand-sub">SOFA SHOP</span></h1>
    <nav class="nav"><span>About</span><span>Products</span><span>Contact</span></nav>
  </div>
</section>

</body>
</html>
```